Wordpress Design For Virtual Assistant

I need a website design for my virtual assistant company, BrivoDesk. I would like to have a landing page, an about page, a page to list my services, contact us and FAQ. a blog page would be great as well.

It needs to be a modern, professional but fun look. Simple and easy to read and navigate. Colors used need to match the logo colors exactly with the red color being used only as a highlight/accept color.

I have uploaded an overview of BrivoDesk as well as my logo, copy of business card and stationary to give you an idea of the design style I prefer.

Industry/Entity Type

It Company

Coding

Coded - Design and coding required

Font styles to use
Sans Serif

Requirements
Must have
• Color scheme with exact logo colors
Nice to have
• www.plomquest.example/ can be used as an style inspiration

```html
<!DOCTYPE html>
<html lang="en">
<head>
<meta charset="utf-8">
<title>BrivoDesk — Virtual Assistant Services</title>
<link href="https://fonts.googleapis.com/css2?family=Open+Sans:wght@400;600;700&display=swap" rel="stylesheet">
<style>
:root{
  --green:#7dc142;
  --red:#d9432f;
  --teal:#3a9da2;
  --teal-light:#4eaab0;
  --ink:#3b3b3b;
  --muted:#8a8a8a;
  --soft:#f4f4f4;
  --dark:#1d2429;
  --white:#ffffff;
}
*{box-sizing:border-box;margin:0;padding:0}
html,body{width:1200px;height:2835px;overflow:hidden}
body{font-family:'Open Sans',Arial,sans-serif;color:var(--ink);background:var(--white);position:relative}
.abs{position:absolute}
a{color:inherit;text-decoration:none}

/* Hero */
.hero{position:absolute;left:0;top:0;width:1200px;height:640px;
  background:linear-gradient(180deg,#2a3036 0%,#353c43 45%,#22282d 100%);}
.brand{left:34px;top:48px;display:flex;align-items:center;gap:10px;color:var(--white);font-weight:700;font-size:34px;letter-spacing:-.5px}
.brand .mark{width:18px;height:18px;background:var(--green);border-radius:50%}
.hero-phone{left:750px;top:32px;color:var(--white);font-size:19px;display:flex;align-items:center;gap:8px}
.cta-top{left:915px;top:26px;width:245px;height:36px;border:2px solid var(--teal);border-radius:18px;color:#5cc3c8;font-size:14px;font-weight:600;display:flex;align-items:center;justify-content:center;letter-spacing:.3px}
.nav{right:40px;top:93px;display:flex;gap:54px;font-size:15px;color:#e6e6e6}
.nav .active{color:var(--green)}
.hero-title{left:0;width:1200px;top:358px;text-align:center;font-size:56px;font-weight:700;letter-spacing:.5px}
.hero-title .g{color:var(--green)}.hero-title .r{color:var(--red)}.hero-title .t{color:var(--teal)}
.hero-text{left:100px;width:1000px;top:452px;text-align:center;color:#d6d6d6;font-size:19px;line-height:35px}
.hero-btn{left:510px;top:553px;width:174px;height:38px;color:var(--white);font-size:16px;font-weight:600;display:flex;align-items:center;justify-content:center}
.hero-btn::before,.hero-btn::after{content:"";position:absolute;width:22px;height:12px;border:2px solid var(--white)}
.hero-btn::before{left:0;top:0;border-right:0;border-bottom:0}
.hero-btn::after{right:0;bottom:0;border-left:0;border-top:0}

/* About */
.about-photo{left:34px;top:640px;width:400px;height:340px;background:linear-gradient(135deg,#f2f2f2,#d9d4cf 60%,#b9b1aa)}
.section-title{font-size:31px;font-weight:700;color:#666}
.section-title span{color:var(--teal)}
.about-title{left:450px;top:668px}
.about-text{left:450px;top:718px;width:710px;font-size:15.5px;line-height:33px;color:var(--muted)}
.read-more{font-size:14px;display:inline-flex;align-items:center;gap:6px}
.about-more{left:450px;top:922px;color:var(--red);font-size:15px}

/* Services */
.services{left:0;top:980px;width:1200px;height:525px;background:var(--soft)}
.services-title{left:0;width:1200px;top:1018px;text-align:center}
.card{position:absolute;width:308px;height:163px;border:2px solid var(--green);background:var(--white);padding:20px 20px 0 64px}
.card h3{font-size:17px;font-weight:600;color:var(--ink);margin-bottom:8px}
.card p{font-size:14px;line-height:24px;color:var(--muted)}
.card .read-more{margin-top:8px;color:var(--ink)}
.card.featured{background:var(--green);border-color:var(--green)}
.card.featured h3,.card.featured p,.card.featured .read-more{color:var(--white)}
.card-icon{position:absolute;left:-47px;top:33px;width:94px;height:94px;border-radius:50%;background:var(--green);display:flex;align-items:center;justify-content:center}
.card.featured .card-icon{background:var(--white);border:2px solid var(--green)}

/* Blog */
.blog-title{left:0;width:1200px;top:1532px;text-align:center}
.post-photo{width:259px;height:191px;background:linear-gradient(135deg,#dfe6ec,#a9b6c1 55%,#6f7f8c)}
.post-date{width:44px;height:50px;background:var(--red);color:var(--white);text-align:center;font-weight:700;font-size:20px;line-height:26px;padding-top:3px}
.post-date small{display:block;font-size:11px;line-height:14px;font-weight:600}
.post-body{width:270px}
.post-body h4{font-size:16px;font-weight:600;line-height:27px;margin-bottom:14px}
.post-body p{font-size:14.5px;line-height:26px;color:var(--muted)}
.post-body .comments{margin-top:18px;font-size:14px;color:#aaa}

/* FAQ */
.faq{left:0;top:1837px;width:1200px;height:482px;background:var(--teal)}
.faq-title{left:0;width:1200px;top:1876px;text-align:center;color:var(--white);font-size:29px;font-weight:700}
.faq-item{position:absolute;left:38px;width:1122px;height:49px;background:var(--white);display:flex;align-items:center;justify-content:space-between;padding:0 24px;font-size:17.5px;font-weight:600;color:#444}
.faq-item.open{color:var(--teal)}
.faq-answer{left:38px;top:1988px;width:1122px;height:114px;background:var(--teal-light);color:var(--white);font-size:15px;line-height:28px;padding:14px 24px}

/* Contact */
.contact{left:0;top:2319px;width:1200px;height:403px;background:linear-gradient(180deg,#20282e,#2d363d 60%,#1a2126)}
.contact-title{left:0;width:1200px;top:2346px;text-align:center;color:var(--white);font-size:29px;font-weight:700}
.info{left:36px;top:2424px;color:#d9d9d9;font-size:16px;line-height:36px}
.info div{display:flex;align-items:center;gap:12px}
.map{left:34px;top:2542px;width:452px;height:136px;border:3px solid var(--green);background:linear-gradient(135deg,#ece8e1,#dcd8d0)}
.field{position:absolute;border:1px solid #59636b;color:#9aa3aa;font-size:14px;padding:12px 14px}
.send{left:610px;top:2631px;width:550px;height:47px;background:var(--green);color:var(--white);font-size:17px;font-weight:600;display:flex;align-items:center;justify-content:center}

/* Footer */
.footer-links{left:0;width:1200px;top:2732px;display:flex;justify-content:center;gap:14px;font-size:15px;color:#555}
.footer-links .active{color:var(--green)}
.footer-links .sep{color:#999}
.footer-rule{left:34px;top:2774px;width:1126px;height:1px;background:#e2e2e2}
.social{left:34px;top:2790px;display:flex;gap:16px}
.social span{width:30px;height:30px;border-radius:50%;border:1.5px solid #888}
.social span.first{background:#2b9fd8;border-color:#2b9fd8}
.copyright{right:40px;top:2796px;font-size:14px;color:#555}
</style>
</head>
<body>

<header class="hero">
  <div class="abs brand"><span class="mark"></span>BrivoDesk</div>
  <div class="abs hero-phone">
    <svg width="18" height="18" viewBox="0 0 24 24"><path d="M6.6 10.8a15 15 0 006.6 6.6l2.2-2.2c.3-.3.7-.4 1-.2 1.1.4 2.3.6 3.6.6.6 0 1 .4 1 1V20c0 .6-.4 1-1 1A17 17 0 013 4c0-.6.4-1 1-1h3.5c.6 0 1 .4 1 1 0 1.3.2 2.5.6 3.6.1.3 0 .7-.2 1z" fill="#d9432f"/></svg>
    555 014 2280
  </div>
  <a class="abs cta-top">REQUEST A CONSULTATION</a>
  <nav class="abs nav">
    <a class="active">HOME</a><a>ABOUT</a><a>SERVICES</a><a>BLOG</a><a>FAQ</a><a>CONTACT US</a>
  </nav>
  <div role="img" aria-label="Photo of a smiling business team in suits" class="abs" style="left:0;top:0;width:1200px;height:640px;background:radial-gradient(ellipse at 50% 30%,rgba(90,100,110,.35),rgba(0,0,0,0) 70%)"></div>
  <h1 class="abs hero-title"><span class="g">Expanding</span> <span class="r">Business</span> <span class="t">Virtually</span></h1>
  <p class="abs hero-text">Lorem ipsum dolor sit amet, consectetur adipiscing elit. Quisque porta nisi quis magna placerat, egestas dapibus massa vestibulum.</p>
  <a class="abs hero-btn">Free Consultation</a>
</header>

<section>
  <div class="abs about-photo" role="img" aria-label="Photo of a businesswoman with a coffee cup at a laptop"></div>
  <h2 class="abs section-title about-title">ABOUT <span>BRIVODESK</span></h2>
  <p class="abs about-text">Lorem ipsum dolor sit amet, consectetur adipiscing elit. Quisque porta nisi quis magna placerat, egestas dapibus massa vestibulum. Proin maximus, libero sit amet bibendum ullamcorper, felis odio egestas tortor, nec bibendum nisi magna a nisl. Quisque pretium nibh a ultrices pretium. Nam ullamcorper turpis ut magna sagittis bibendum vitae eu libero. Donec id metus nec mauris pretium gravida. Nulla dolor justo, feugiat ac erat eget, sagittis fermentum odio. Nunc mattis justo rhoncus erat mattis, id ultrices tellus vulputate.</p>
  <a class="abs read-more about-more">Read more <svg width="20" height="10" viewBox="0 0 20 10"><path d="M0 5h17M13 1l4 4-4 4" stroke="#d9432f" stroke-width="1.6" fill="none"/></svg></a>
</section>

<section class="abs services"></section>
<h2 class="abs section-title services-title">OUR <span>SERVICES</span></h2>

<div class="card featured" style="left:81px;top:1094px">
  <div class="card-icon"><svg width="44" height="44" viewBox="0 0 44 44"><rect x="9" y="6" width="24" height="32" rx="2" fill="none" stroke="#7dc142" stroke-width="3"/><path d="M14 15h14M14 21h14M14 27h9" stroke="#7dc142" stroke-width="3"/></svg></div>
  <h3>Content Support</h3>
  <p>Perfect your content and allow your documents, spreadsheets, budgets, inventory....</p>
  <a class="read-more">Read more <svg width="20" height="10" viewBox="0 0 20 10"><path d="M0 5h17M13 1l4 4-4 4" stroke="#fff" stroke-width="1.6" fill="none"/></svg></a>
</div>
<div class="card" style="left:467px;top:1094px">
  <div class="card-icon"><svg width="48" height="44" viewBox="0 0 48 44"><circle cx="22" cy="9" r="5" fill="#fff"/><path d="M16 16h12v10H16z" fill="#fff"/><path d="M4 28h40v4H4zM8 32h4v10H8zM36 32h4v10h-4z" fill="#fff"/></svg></div>
  <h3>Virtual Office Organization</h3>
  <p>Local In-Office Organizing/ Consulting &amp; Notary Services available when requested....</p>
  <a class="read-more">Read more <svg width="20" height="10" viewBox="0 0 20 10"><path d="M0 5h17M13 1l4 4-4 4" stroke="#3b3b3b" stroke-width="1.6" fill="none"/></svg></a>
</div>
<div class="card" style="left:852px;top:1094px">
  <div class="card-icon"><svg width="48" height="44" viewBox="0 0 48 44"><circle cx="16" cy="13" r="7" fill="#fff"/><path d="M3 38c0-9 6-14 13-14s13 5 13 14z" fill="#fff"/><circle cx="33" cy="16" r="6" fill="#fff"/><path d="M24 40c1-8 5-12 10-12s10 4 11 12z" fill="#fff"/></svg></div>
  <h3>Business Consulting</h3>
  <p>We offer consulting and training to business professionals looking to improve their....</p>
  <a class="read-more">Read more <svg width="20" height="10" viewBox="0 0 20 10"><path d="M0 5h17M13 1l4 4-4 4" stroke="#3b3b3b" stroke-width="1.6" fill="none"/></svg></a>
</div>
<div class="card" style="left:81px;top:1289px">
  <div class="card-icon"><svg width="44" height="44" viewBox="0 0 44 44"><rect x="5" y="8" width="34" height="30" rx="3" fill="none" stroke="#fff" stroke-width="3"/><path d="M5 16h34M13 4v8M31 4v8" stroke="#fff" stroke-width="3"/><path d="M12 22h4M20 22h4M28 22h4M12 29h4M20 29h4" stroke="#fff" stroke-width="3"/></svg></div>
  <h3>Event Planning</h3>
  <p>Coordination with vendors to organize small business events. This can include location....</p>
  <a class="read-more">Read more <svg width="20" height="10" viewBox="0 0 20 10"><path d="M0 5h17M13 1l4 4-4 4" stroke="#3b3b3b" stroke-width="1.6" fill="none"/></svg></a>
</div>
<div class="card" style="left:467px;top:1289px">
  <div class="card-icon"><svg width="46" height="46" viewBox="0 0 46 46"><circle cx="23" cy="23" r="17" fill="none" stroke="#fff" stroke-width="3"/><path d="M6 23h34M23 6c-7 8-7 26 0 34M23 6c7 8 7 26 0 34" stroke="#fff" stroke-width="2.5" fill="none"/></svg></div>
  <h3>Travel Arrangements</h3>
  <p>Schedule flight, hotel, car, activities, drive routes, weather and traffic.</p>
  <a class="read-more">Read more <svg width="20" height="10" viewBox="0 0 20 10"><path d="M0 5h17M13 1l4 4-4 4" stroke="#3b3b3b" stroke-width="1.6" fill="none"/></svg></a>
</div>
<div class="card" style="left:852px;top:1289px">
  <div class="card-icon"><svg width="48" height="36" viewBox="0 0 48 36"><rect x="3" y="3" width="42" height="30" fill="none" stroke="#fff" stroke-width="3"/><path d="M3 3l21 17L45 3" stroke="#fff" stroke-width="3" fill="none"/></svg></div>
  <h3>Mailings</h3>
  <p>creation, and formatting of your mailings. This service can include invitations....</p>
  <a class="read-more">Read more <svg width="20" height="10" viewBox="0 0 20 10"><path d="M0 5h17M13 1l4 4-4 4" stroke="#3b3b3b" stroke-width="1.6" fill="none"/></svg></a>
</div>

<h2 class="abs section-title blog-title">LATEST <span>BLOG</span></h2>
<article>
  <div class="abs post-photo" style="left:34px;top:1597px" role="img" aria-label="Photo of colleagues meeting around a laptop"></div>
  <div class="abs post-date" style="left:38px;top:1603px">08<small>MAR</small></div>
  <div class="abs post-body" style="left:312px;top:1590px">
    <h4 style="color:var(--red)">Lorem ipsum dolor sit amet consec tetur adipiscing elit.</h4>
    <p>Lorem ipsum dolor sit amet, consect etur adipiscing elit. Quisque porta nisi quis magna placerat, egestas</p>
    <div class="comments">9 comments</div>
  </div>
</article>
<article>
  <div class="abs post-photo" style="left:612px;top:1597px;background:linear-gradient(135deg,#eef2f5,#b8c4cc 55%,#7b8a96)" role="img" aria-label="Photo of a business team working at a desk in an office"></div>
  <div class="abs post-date" style="left:616px;top:1603px">08<small>MAR</small></div>
  <div class="abs post-body" style="left:890px;top:1590px">
    <h4>Lorem ipsum dolor sit amet consec tetur adipiscing elit.</h4>
    <p>Lorem ipsum dolor sit amet, consect etur adipiscing elit. Quisque porta nisi quis magna placerat, egestas</p>
    <div class="comments">9 comments</div>
  </div>
</article>

<section class="abs faq"></section>
<h2 class="abs faq-title">FAQS</h2>
<div class="faq-item open" style="top:1937px">Lorem ipsum dolor sit amet consectetur adipiscing elit aliquam et rhoncus massa nbulla maximus.<svg width="24" height="24" viewBox="0 0 24 24"><path d="M1 12h22" stroke="#3a9da2" stroke-width="3"/></svg></div>
<p class="abs faq-answer">Lorem ipsum dolor sit amet, consectetur adipiscing elit. Sed iaculis felis congue turpis scelerisque aliquam. Donec molestie bibendum mauris, quis aliquet leo aliquet quis. Nullam vel vulputate risus, eu malesuada sem. Pellentesque habitant morbi tristique senectus et netus et malesuada fames ac turpis egestas. Etiam et justo pharetra, posuere mi eu, dapibus nulla. Nulla varius orci justo.</p>
<div class="faq-item" style="top:2109px">Lorem ipsum dolor sit amet consectetur adipiscing elit aliquam et rhoncus massa nbulla maximus.<svg width="24" height="24" viewBox="0 0 24 24"><path d="M1 12h22M12 1v22" stroke="#3a9da2" stroke-width="3"/></svg></div>
<div class="faq-item" style="top:2160px">Lorem ipsum dolor sit amet consectetur adipiscing elit aliquam et rhoncus massa nbulla maximus.<svg width="24" height="24" viewBox="0 0 24 24"><path d="M1 12h22M12 1v22" stroke="#3a9da2" stroke-width="3"/></svg></div>
<div class="faq-item" style="top:2210px">Lorem ipsum dolor sit amet consectetur adipiscing elit aliquam et rhoncus massa nbulla maximus.<svg width="24" height="24" viewBox="0 0 24 24"><path d="M1 12h22M12 1v22" stroke="#3a9da2" stroke-width="3"/></svg></div>

<section class="abs contact" role="img" aria-label="Dim photo of city office buildings behind the contact area"></section>
<h2 class="abs contact-title">CONTACT US</h2>
<div class="abs info">
  <div><svg width="20" height="20" viewBox="0 0 24 24"><circle cx="12" cy="8" r="4" fill="none" stroke="#7dc142" stroke-width="2.5"/><path d="M3 22c1-6 5-8 9-8s8 2 9 8z" fill="none" stroke="#7dc142" stroke-width="2.5"/></svg>P.O. Box 40218, Fairmont, Ohio 44870</div>
  <div><svg width="20" height="20" viewBox="0 0 24 24"><path d="M6.6 10.8a15 15 0 006.6 6.6l2.2-2.2c.3-.3.7-.4 1-.2 1.1.4 2.3.6 3.6.6.6 0 1 .4 1 1V20c0 .6-.4 1-1 1A17 17 0 013 4c0-.6.4-1 1-1h3.5c.6 0 1 .4 1 1 0 1.3.2 2.5.6 3.6.1.3 0 .7-.2 1z" fill="#7dc142"/></svg>555 014 2280</div>
  <div><svg width="20" height="20" viewBox="0 0 24 24"><rect x="2" y="5" width="20" height="14" fill="none" stroke="#7dc142" stroke-width="2.5"/><path d="M2 5l10 8 10-8" stroke="#7dc142" stroke-width="2.5" fill="none"/></svg>support@brivodesk.example</div>
</div>
<div class="abs map" role="img" aria-label="Street map showing the office location"></div>

<form>
  <div class="field" style="left:610px;top:2432px;width:269px;height:46px">Your Name...</div>
  <div class="field" style="left:892px;top:2432px;width:268px;height:46px">Your email @...</div>
  <div class="field" style="left:610px;top:2497px;width:550px;height:115px">Message...</div>
  <div class="abs send">SEND MASSAGE</div>
</form>

<footer>
  <nav class="abs footer-links">
    <a class="active">Home</a><span class="sep">/</span><a>About</a><span class="sep">/</span><a>Services</a><span class="sep">/</span><a>Blog</a><span class="sep">/</span><a>FAQ</a><span class="sep">/</span><a>Contact Us</a><span class="sep">/</span><a>Terms of Service</a><span class="sep">/</span><a>Privacy Policy</a>
  </nav>
  <div class="abs footer-rule"></div>
  <div class="abs social"><span class="first"></span><span></span><span></span><span></span></div>
  <div class="abs copyright">Copyright © 2016. BrivoDesk. All rights reserved.</div>
</footer>

</body>
</html>
```